Baked goods front of bag sticker

Pebblecrest Brownies,
2 Go size (clear plastic bag of handful of ¼” square bites)
There will also be larger sizes and custom options(corporate/events) using the same image.
Deliverables Needed:
Need sticker with “Pebblecrest Brownies” for front of bag, approximate 2” circle or rectangle/square.
Packaging front sticker design should be sizable for other media, ie website, future packaging, logo.
Flavor should be indicated on second sticker that integrates well.
Back sticker is already complete and includes ingredients, company name, health dept permit, and other legal necessities. Font will be changed to integrate with front.
Flavors:
1. Sunset Maple Brownie
2. Honeycomb Glow Brownie
3. Zip Zop Mint
4. Crumbly Oat Delight (not so gooey but great)
Primary Audiences:
Anyone who wants a sweet treat to enjoy, and maybe share, on the go. Audience wants a fresh treat with real ingredients they know and love (real butter, Pure vanilla, Fresh eggs)
Audience wants something from a baker not a machine.
Sold at checkout in stores that don’t have baked goods, higher end convenience stores, specialty stores, small gourmet stores, theaters, toy stores, sports arenas, etc.
Will be sampled at events (festivals, movie screenings, races)
Tone and Image:
Fresh, Fun and frank with real ingredients you know
Because it is little and is home-baked, it should be perceived as a little treat without the guilt.
Messages:
Fresh, natural, little treat on the run.
Dear Designers,

```html
<!DOCTYPE html>
<html lang="en">
<head>
<meta charset="utf-8">
<title>Pebblecrest Brownies – Sticker Set</title>
<link rel="stylesheet" href="https://fonts.googleapis.com/css2?family=Big+Shoulders+Display:wght@600;700&family=Yellowtail&display=swap">
<style>
  :root {
    --page: #ffffff;
    --cocoa: #3b2417;
    --cream: #f7dcb0;
    --ember: #e0562b;
    --ember-soft: #ee6f4b;
    --rosewood: #d08e78;
    --maple-rim: #3e2416;
    --maple-face: #7b4a3a;
    --maple-glow: #8a5440;
    --maple-script: #c98f7a;
    --maple-title: #f07650;
    --mint-rim: #ee4a4d;
    --mint-face: #f48f85;
    --mint-bang: #ef7450;
    --oat-rim: #ee7049;
    --oat-face: #f59a54;
    --oat-icon: #e0895e;
    --dots: rgba(255, 240, 225, 0.85);
  }
  html, body {
    margin: 0;
    width: 1200px;
    height: 1000px;
    overflow: hidden;
    background: var(--page);
  }
  .sticker-sheet { display: block; width: 1200px; height: 1000px; }
  .display-type {
    font-family: "Big Shoulders Display", "Arial Narrow", sans-serif;
    font-weight: 700;
    text-anchor: middle;
    letter-spacing: 1px;
  }
  .script-type {
    font-family: "Yellowtail", cursive;
    text-anchor: middle;
  }
  .dotted-ring {
    fill: none;
    stroke: var(--dots);
    stroke-width: 2;
    stroke-dasharray: 1 6;
    stroke-linecap: round;
  }
</style>
</head>
<body>
<svg class="sticker-sheet" viewBox="0 0 1200 1000" xmlns="http://www.w3.org/2000/svg">
  <defs>
    <filter id="lift" x="-10%" y="-10%" width="125%" height="125%">
      <feDropShadow dx="3" dy="5" stdDeviation="5" flood-color="#000" flood-opacity="0.22"/>
    </filter>
    <linearGradient id="ember-text" x1="0" x2="1">
      <stop offset="0" stop-color="#e8512a"/>
      <stop offset="1" stop-color="#f2784f"/>
    </linearGradient>
    <radialGradient id="maple-burst" cx="0.5" cy="0.5" r="0.5">
      <stop offset="0.55" stop-color="var(--maple-glow)"/>
      <stop offset="1" stop-color="var(--maple-face)"/>
    </radialGradient>
  </defs>

  <!-- Honeycomb Glow flavour sticker -->
  <g class="flavour-sticker flavour-honeycomb" filter="url(#lift)">
    <circle cx="228" cy="232" r="205" fill="var(--ember)"/>
    <circle cx="228" cy="232" r="192" fill="var(--ember-soft)"/>
    <circle class="dotted-ring" cx="228" cy="232" r="188"/>
  </g>
  <text class="display-type" x="228" y="180" font-size="54" fill="var(--cocoa)" textLength="285" lengthAdjust="spacingAndGlyphs">HONEYCOMB</text>
  <text class="display-type" x="228" y="328" font-size="160" fill="var(--cream)" textLength="275" lengthAdjust="spacingAndGlyphs">GLOW</text>

  <!-- Sunset Maple flavour sticker -->
  <g class="flavour-sticker flavour-maple" filter="url(#lift)">
    <circle cx="980" cy="212" r="205" fill="var(--maple-rim)"/>
    <circle cx="980" cy="212" r="188" fill="url(#maple-burst)" role="img" aria-label="Soft starburst glow behind the flavour name"/>
    <circle class="dotted-ring" cx="980" cy="212" r="186"/>
  </g>
  <text class="script-type" x="978" y="188" font-size="96" fill="var(--maple-script)" textLength="270" lengthAdjust="spacingAndGlyphs" transform="rotate(-6 978 168)">Sunset</text>
  <text class="display-type" x="980" y="305" font-size="116" fill="var(--maple-title)" textLength="295" lengthAdjust="spacingAndGlyphs">MAPLE</text>

  <!-- Main brand sticker -->
  <g class="brand-sticker" filter="url(#lift)">
    <circle cx="612" cy="473" r="217" fill="var(--rosewood)"/>
    <circle cx="612" cy="473" r="200" fill="var(--cocoa)"/>
  </g>
  <text class="display-type brand-name" x="612" y="462" font-size="76" fill="url(#ember-text)" textLength="340" lengthAdjust="spacingAndGlyphs">PEBBLECREST</text>
  <text class="display-type brand-product" x="612" y="552" font-size="92" fill="var(--rosewood)" textLength="340" lengthAdjust="spacingAndGlyphs">BROWNIES</text>

  <!-- Zip Zop Mint flavour sticker -->
  <g class="flavour-sticker flavour-mint" filter="url(#lift)">
    <circle cx="220" cy="748" r="205" fill="var(--mint-rim)"/>
    <circle cx="220" cy="748" r="190" fill="var(--mint-face)"/>
    <circle class="dotted-ring" cx="220" cy="748" r="186"/>
  </g>
  <text class="display-type" x="118" y="712" font-size="64" fill="var(--cocoa)" transform="rotate(-4 118 690)">ZIP</text>
  <g class="exclamation" fill="var(--mint-bang)" stroke="var(--cocoa)" stroke-width="4">
    <path d="M208 610 Q233 582 258 610 L246 758 L220 758 Z"/>
    <circle cx="233" cy="774" r="6" fill="var(--cocoa)" stroke="none"/>
  </g>
  <text class="display-type" x="325" y="738" font-size="64" fill="var(--cocoa)" transform="rotate(4 325 718)">ZOP</text>
  <text class="display-type" x="220" y="868" font-size="72" fill="var(--cocoa)" textLength="190" lengthAdjust="spacingAndGlyphs">MINT</text>

  <!-- Crumbly Oat Delight flavour sticker -->
  <g class="flavour-sticker flavour-oat" filter="url(#lift)">
    <circle cx="970" cy="790" r="205" fill="var(--oat-rim)"/>
    <circle cx="970" cy="790" r="190" fill="var(--oat-face)"/>
    <circle class="dotted-ring" cx="970" cy="790" r="186"/>
  </g>
  <text class="script-type" x="925" y="710" font-size="72" fill="var(--cream)" textLength="210" lengthAdjust="spacingAndGlyphs" transform="rotate(-35 925 710)">Crumbly</text>
  <rect class="thumb-illustration" x="925" y="752" width="95" height="90" rx="14" fill="var(--oat-icon)" role="img" aria-label="Thumbs-up hand illustration"/>
  <text class="display-type" x="970" y="902" font-size="56" fill="var(--cocoa)" textLength="265" lengthAdjust="spacingAndGlyphs">OAT DELIGHT</text>
</svg>
</body>
</html>
```